Bref créative
Brisk Lattice Cards & Stationary
Project #2
Corporate
Carl Wendimeer
VP of Business Development
2841 Thornbury Lane
Lindenmoor, QX 55612
cwendimeer@brisklattice-mail.com
www.brisklattice-mail.com
Here is our logo

```html
<!DOCTYPE html>
<html lang="en">
<head>
<meta charset="utf-8">
<title>Brisk Lattice – Business Card</title>
<link href="https://fonts.googleapis.com/css2?family=Arimo:wght@400;700&display=swap" rel="stylesheet">
<style>
  :root {
    --page: #ffffff;
    --card-white: #ffffff;
    --card-dark: #3f4345;
    --band-dark: #45494b;
    --accent-blue: #1e7fd0;
    --accent-line: #3aa0e8;
    --ink: #1c1c1c;
    --ink-soft: #333333;
    --text-light: #f2f2f2;
    --rule-light: #d8d8d8;
  }
  * { margin: 0; padding: 0; box-sizing: border-box; }
  html, body {
    width: 1200px;
    height: 678px;
    overflow: hidden;
    background: var(--page);
    font-family: "Arimo", Arial, sans-serif;
  }
  .canvas { position: relative; width: 1200px; height: 678px; }

  .card { position: absolute; width: 620px; height: 352px; overflow: hidden; }

  /* Back card */
  .card-back {
    left: 580px; top: 326px;
    background: var(--card-dark);
  }
  .back-brand {
    position: absolute; left: 0; right: 0; top: 138px;
    display: flex; align-items: center; justify-content: center; gap: 16px;
  }
  .back-brand .mark {
    width: 54px; height: 54px; border-radius: 50%;
    background: var(--accent-blue);
  }
  .back-brand .name {
    font-size: 44px; font-weight: 700; color: var(--accent-blue);
    letter-spacing: 1px; line-height: 1;
  }
  .back-web {
    position: absolute; left: 0; right: 0; top: 268px;
    display: flex; align-items: center; justify-content: center; gap: 12px;
    color: var(--text-light); font-size: 17px;
  }
  .back-web .rule { width: 76px; height: 2px; background: var(--rule-light); }

  /* Front card */
  .card-front {
    left: 0; top: 0;
    background: var(--card-white);
    box-shadow: 0 0 0 1px #e2e2e2;
    z-index: 2;
  }
  .front-brand {
    position: absolute; left: 42px; top: 48px;
    display: flex; align-items: center; gap: 12px;
  }
  .front-brand .mark {
    width: 38px; height: 38px; border-radius: 50%;
    background: var(--accent-blue);
  }
  .front-brand .name {
    font-size: 27px; font-weight: 700; color: var(--accent-blue); line-height: 1;
  }
  .person {
    position: absolute; left: 0; width: 624px; top: 170px;
    text-align: center; color: var(--ink);
  }
  .person .full-name { font-size: 25px; font-weight: 700; }
  .person .job-title { font-size: 17px; color: var(--ink-soft); margin-top: 6px; }

  .contact-band {
    position: absolute; left: 0; right: 0; top: 272px; bottom: 0;
    background: var(--band-dark);
    border-top: 3px solid var(--accent-line);
    color: var(--text-light); font-size: 15.5px; line-height: 19px;
  }
  .contact-band .address { position: absolute; left: 24px; top: 8px; }
  .contact-band .direct { position: absolute; left: 318px; top: 8px; }
  .contact-band .website {
    position: absolute; left: 0; right: 0; top: 51px;
    text-align: center; font-size: 17px;
  }
</style>
</head>
<body>
<div class="canvas">

  <section class="card card-back">
    <div class="back-brand">
      <span class="mark"></span>
      <span class="name">Brisk Lattice</span>
    </div>
    <div class="back-web">
      <span class="rule"></span>
      <span>www.brisklattice-mail.com</span>
      <span class="rule"></span>
    </div>
  </section>

  <section class="card card-front">
    <div class="front-brand">
      <span class="mark"></span>
      <span class="name">Brisk Lattice</span>
    </div>
    <div class="person">
      <p class="full-name">Carl Wendimeer</p>
      <p class="job-title">VP of Business Development</p>
    </div>
    <div class="contact-band">
      <p class="address">2841 Thornbury Lane<br>Lindenmoor, QX 55612</p>
      <p class="direct">C: 612-555-0147<br>E: cwendimeer@brisklattice-mail.com</p>
      <p class="website">www.brisklattice-mail.com</p>
    </div>
  </section>

</div>
</body>
</html>
```